Wandelow valley aerial works business card size advertising

I’m after a simple design , please see attached photo . Im after the same color green in the photo as the base color and the the little white man but instead of him holding a spanner i would like him to be holding a tv antenna pointing an angle , see attached photo of the antenna , i would like him on the left of the business card and the business name to fit in on the right with the phone number . ( if the antenna idea looks stupid , leave him holding a spanner ) On the reverse side of the card i would like a white background with green writing stating some of the services we provide which are the following .Antenna installations and repairs Wall mounting of tv’s Additional TV outlets Orbix satellite supply and installations Wandelow , Brimsdale , Kerrawin , Mundoora , Tellbrook , Oxley Flat , All rural areas All in all i would like the business card to compliment my invoices as pictured “ invoice supplied is a dummy invoice “

wandelow valley aerial works 0491836527

Sans Serif

9bcb3c

• what i ask for in project description

```html
<!DOCTYPE html>
<html lang="en">
<head>
<meta charset="utf-8">
<title>Wandelow Valley Aerial Works – Business Cards</title>
<link rel="stylesheet" href="https://fonts.googleapis.com/css2?family=Ubuntu:wght@400;500;700&display=swap">
<style>
  :root {
    --brand-green: #9bcb3c;
    --edge-green: #7fae2c;
    --ink: #4a4a4a;
    --card-white: #f2f3f1;
    --backdrop: #e9e6e2;
  }
  * { box-sizing: border-box; margin: 0; padding: 0; }
  html, body {
    width: 1200px;
    height: 1137px;
    overflow: hidden;
    background: var(--backdrop);
    font-family: "Ubuntu", sans-serif;
  }
  .sheet {
    position: relative;
    width: 1200px;
    height: 1137px;
  }
  .card {
    position: absolute;
    left: 240px;
    width: 720px;
    height: 440px;
    background: var(--card-white);
    border: 3px solid var(--edge-green);
    overflow: hidden;
  }
  .card--back { top: 70px; }
  .card--front { top: 610px; }

  .brand-square {
    position: absolute;
    width: 170px;
    height: 150px;
    background: var(--brand-green);
  }
  .card--back .brand-square { left: 480px; top: 40px; }
  .card--front .brand-square { left: 420px; top: 70px; }

  .brand-name {
    position: absolute;
    color: var(--ink);
    font-weight: 700;
    font-size: 28px;
    letter-spacing: 1px;
    line-height: 1.2;
    text-transform: uppercase;
    white-space: nowrap;
  }
  .card--back .brand-name { right: 260px; top: 122px; text-align: right; font-size: 26px; }
  .card--front .brand-name { left: 150px; top: 240px; }

  .phone {
    position: absolute;
    left: 150px;
    top: 335px;
    display: flex;
    align-items: center;
    gap: 14px;
    color: var(--ink);
    font-size: 40px;
    font-weight: 400;
    letter-spacing: 1px;
    line-height: 1;
  }
  .phone svg { width: 24px; height: 32px; flex: none; }

  .services {
    position: absolute;
    left: 60px;
    right: 60px;
    top: 228px;
    color: var(--ink);
    font-size: 18px;
    font-weight: 500;
    line-height: 1.5;
    list-style: none;
  }
  .service-band {
    position: absolute;
    left: 0;
    right: 0;
    bottom: 36px;
    height: 38px;
    background: var(--brand-green);
    color: #ffffff;
    font-size: 16px;
    display: flex;
    align-items: center;
    padding-left: 40px;
    white-space: nowrap;
  }
</style>
</head>
<body>
<main class="sheet">
  <section class="card card--back" aria-label="Business card, reverse side">
    <div class="brand-square"></div>
    <h2 class="brand-name">Wandelow Valley<br>Aerial Works</h2>
    <ul class="services">
      <li>Antenna installations and repairs Wall mounting of tv’s</li>
      <li>Additional TV outlets Orbix satellite supply and installations</li>
    </ul>
    <p class="service-band">Wandelow, Brimsdale, Kerrawin, Mundoora, Tellbrook, Oxley Flat, All rural areas</p>
  </section>

  <section class="card card--front" aria-label="Business card, front side">
    <div class="brand-square"></div>
    <h1 class="brand-name">Wandelow Valley<br>Aerial Works</h1>
    <p class="phone">
      <svg viewBox="0 0 26 34" aria-hidden="true">
        <path d="M7 2 L12 2 L13 10 L9 12 Q10 20 14 24 L18 21 L23 25 L21 31 Q14 33 8 25 Q2 16 4 6 Z" fill="var(--brand-green)"/>
      </svg>
      <span>0491836527</span>
    </p>
  </section>
</main>
</body>
</html>
```